Promotional business a5 Notepad design

I am looking for a custom a5 notepad design as a promotional item to give away to customers etc.
Attached will be a desk planner we had designed feel free to use as a reference.
We want the notepad to have lines running horizontal not squares like the desk planner example.

Industry/Entity Type

Hydraulic / industrial

Colors

Designer to choose colors to be used in the design.

```html
<!DOCTYPE html>
<html lang="en">
<head>
<meta charset="utf-8">
<title>Meridian Hose and Couplings – A5 Notepad</title>
<link rel="stylesheet" href="https://fonts.googleapis.com/css2?family=Arimo:wght@400;700&display=swap">
<style>
  :root {
    --backdrop: #a1a1a3;
    --brand-blue: #142dbf;
    --paper: #ffffff;
    --rule-dark: #3a3a3a;
    --rule-light: #9a9a9a;
    --on-blue: #ffffff;
    --divider: rgba(255,255,255,0.55);
  }
  * { margin: 0; padding: 0; box-sizing: border-box; }
  html, body {
    width: 1200px; height: 900px; overflow: hidden;
    background: var(--backdrop);
    font-family: "Arimo", Arial, sans-serif;
  }
  .notepad {
    position: absolute; left: 325px; top: 60px;
    width: 550px; height: 780px;
    background: var(--paper);
  }
  .notepad-header {
    position: absolute; left: 0; top: 0; width: 100%; height: 111px;
    background: var(--brand-blue);
  }
  .brand {
    position: absolute; left: 62px; top: 31px; width: 236px; height: 58px;
    display: flex; align-items: center; gap: 10px;
  }
  .brand-dot {
    width: 16px; height: 16px; border-radius: 50%;
    background: var(--on-blue); flex: none;
  }
  .brand-name {
    color: var(--on-blue); font-weight: 700; font-size: 17px;
    line-height: 1.15; letter-spacing: 0.5px; text-transform: uppercase;
  }
  .header-divider {
    position: absolute; left: 316px; top: 31px; width: 1px; height: 58px;
    background: var(--divider);
  }
  .contact-list {
    position: absolute; left: 333px; top: 37px; list-style: none;
    color: var(--on-blue); font-size: 12.5px; line-height: 14.5px;
  }
  .contact-list li { display: flex; align-items: center; gap: 4px; }
  .contact-list svg { width: 9px; height: 9px; fill: var(--on-blue); flex: none; }
  .writing-lines {
    position: absolute; left: 38px; top: 157px; width: 474px;
  }
  .writing-lines .rule {
    height: 1px; margin-bottom: 28.5px; background: var(--rule-light);
  }
  .writing-lines .rule:nth-child(odd) { background: var(--rule-light); }
  .writing-lines .rule:nth-child(even) { background: var(--rule-dark); }
  .notepad-footer {
    position: absolute; left: 0; bottom: 0; width: 100%; height: 27px;
    background: var(--brand-blue); color: var(--on-blue);
    display: flex; align-items: center; justify-content: center; gap: 4px;
    font-size: 11px;
  }
  .notepad-footer svg { width: 8px; height: 10px; fill: var(--on-blue); }
</style>
</head>
<body>
  <div class="notepad">
    <header class="notepad-header">
      <div class="brand">
        <span class="brand-dot"></span>
        <span class="brand-name">Meridian Hose<br>and Couplings</span>
      </div>
      <div class="header-divider"></div>
      <ul class="contact-list">
        <li><svg viewBox="0 0 10 10"><path d="M2 0.5 3.6 2.6 2.8 3.6C3.4 5 4.9 6.6 6.4 7.2L7.4 6.4 9.5 8 8.6 9.5C4.5 9 1 5.5 0.5 1.4Z"/></svg>08 7100 4521</li>
        <li><svg viewBox="0 0 10 10"><path d="M2 0.5 3.6 2.6 2.8 3.6C3.4 5 4.9 6.6 6.4 7.2L7.4 6.4 9.5 8 8.6 9.5C4.5 9 1 5.5 0.5 1.4Z"/></svg>0400 123 789</li>
        <li><svg viewBox="0 0 10 10"><path d="M0.5 2h9v6h-9z M0.5 2 5 5.5 9.5 2" stroke="#142dbf" stroke-width="0.8"/></svg>email@meridianhose.com.au</li>
      </ul>
    </header>

    <div class="writing-lines">
      <div class="rule"></div><div class="rule"></div><div class="rule"></div><div class="rule"></div>
      <div class="rule"></div><div class="rule"></div><div class="rule"></div><div class="rule"></div>
      <div class="rule"></div><div class="rule"></div><div class="rule"></div><div class="rule"></div>
      <div class="rule"></div><div class="rule"></div><div class="rule"></div><div class="rule"></div>
      <div class="rule"></div><div class="rule"></div><div class="rule"></div><div class="rule"></div>
    </div>

    <footer class="notepad-footer">
      <svg viewBox="0 0 8 10"><path d="M4 0C1.8 0 0 1.7 0 3.9 0 6.6 4 10 4 10S8 6.6 8 3.9C8 1.7 6.2 0 4 0ZM4 5.4A1.5 1.5 0 1 1 4 2.4 1.5 1.5 0 0 1 4 5.4Z"/></svg>
      Servicing The Adelaide Metropolitan Area
    </footer>
  </div>
</body>
</html>
```